business card letterhead envelope
Darren Holcomb Realtors
Project: business card letterhead envelope
business card letterhead envelope - Real Estate
Creative Brief
Professional
Darren Holcomb
Attorney/Broker
2817 W. Larkspur Ave Suite B7 Brenton Ridge, CO 79748
Darren@PecosPrairieHouses.com
PecosPrairieHouses.com

```html
<!DOCTYPE html>
<html lang="en">
<head>
<meta charset="utf-8">
<title>Darren Holcomb Realtors – Stationery</title>
<link href="https://fonts.googleapis.com/css2?family=Cinzel:wght@400;600&family=Open+Sans:wght@400;600&display=swap" rel="stylesheet">
<style>
  :root {
    --backdrop: #3a3a3a;
    --paper: #ffffff;
    --ink: #1e1e1e;
    --ink-soft: #555555;
    --fold: #d9d9d9;
  }
  * { margin: 0; padding: 0; box-sizing: border-box; }
  html, body { width: 1200px; height: 684px; overflow: hidden; }
  body {
    background: var(--backdrop);
    position: relative;
    font-family: "Open Sans", Arial, sans-serif;
    color: var(--ink);
  }
  .sheet {
    position: absolute;
    background: var(--paper);
    box-shadow: 0 2px 6px rgba(0,0,0,.45);
  }

  /* Brand lockup */
  .brand { display: flex; flex-direction: column; align-items: center; }
  .brand-dot { border-radius: 50%; background: var(--ink); }
  .brand-name {
    font-family: "Cinzel", Georgia, serif;
    font-weight: 600;
    color: var(--ink);
    letter-spacing: .04em;
    text-align: center;
    line-height: 1.15;
    white-space: nowrap;
  }
  .brand-sub {
    font-family: "Cinzel", Georgia, serif;
    font-weight: 600;
    color: var(--ink);
    letter-spacing: .25em;
    text-align: center;
  }

  /* Letterhead */
  .letterhead { left: 206px; top: 29px; width: 413px; height: 631px; }
  .letterhead .brand { margin-top: 22px; }
  .letterhead .brand-dot { width: 30px; height: 30px; margin-bottom: 5px; }
  .letterhead .brand-name { font-size: 11px; }
  .letterhead .brand-sub { font-size: 5px; border-top: 1px solid var(--ink); padding-top: 2px; margin-top: 1px; }
  .footer-line {
    position: absolute; left: 0; right: 0;
    font-size: 5px; color: var(--ink-soft); text-align: center; white-space: nowrap;
  }
  .footer-web { font-weight: 600; color: var(--ink); }
  .letterhead .footer-line { bottom: 26px; }
  .letterhead .footer-web { bottom: 18px; }

  /* Business card */
  .business-card { left: 86px; top: 307px; width: 185px; height: 106px; }
  .business-card .brand { position: absolute; left: 8px; top: 24px; width: 62px; }
  .business-card .brand-dot { width: 17px; height: 17px; margin-bottom: 3px; }
  .business-card .brand-name { font-size: 6px; }
  .business-card .brand-sub { font-size: 3px; }
  .card-details {
    position: absolute; left: 80px; top: 14px;
    font-size: 4.2px; line-height: 1.55; color: var(--ink-soft);
  }
  .card-details .person { font-weight: 600; color: var(--ink); }
  .card-details .spacer { height: 3px; }
  .card-details .web { font-weight: 600; color: var(--ink); }

  /* Envelopes */
  .envelope-back { left: 643px; top: 115px; width: 521px; height: 233px; }
  .flap { position: absolute; inset: 0; }
  .envelope-back .brand { position: absolute; left: 50%; transform: translateX(-50%); top: 118px; }
  .envelope-back .brand-dot { width: 26px; height: 26px; }
  .flap-web {
    position: absolute; left: 0; right: 0; top: 149px;
    text-align: center; font-size: 5px; font-weight: 600;
  }

  .envelope-front { left: 643px; top: 365px; width: 521px; height: 266px; }
  .envelope-front .brand { margin-top: 42px; }
  .envelope-front .brand-dot { width: 28px; height: 28px; margin-bottom: 5px; }
  .envelope-front .brand-name { font-size: 10px; }
  .envelope-front .brand-sub { font-size: 4.5px; border-top: 1px solid var(--ink); padding-top: 2px; margin-top: 1px; }
  .envelope-front .footer-line { left: 10px; right: auto; text-align: left; bottom: 28px; }
  .envelope-front .footer-web { left: 10px; right: auto; text-align: left; bottom: 20px; }
</style>
</head>
<body>

<section class="sheet letterhead">
  <div class="brand">
    <span class="brand-dot"></span>
    <span class="brand-name">Darren Holcomb</span>
    <span class="brand-sub">Realtors</span>
  </div>
  <p class="footer-line">2817 W. Larkspur Ave Suite B7 Brenton Ridge, CO 79748 &nbsp;|&nbsp; P: (555) 201-0148 &nbsp;|&nbsp; F: (555) 201-0162 &nbsp;|&nbsp; C: (555) 201-0177 &nbsp;|&nbsp; E: Darren@PecosPrairieHouses.com</p>
  <p class="footer-line footer-web">www.PecosPrairieHouses.com</p>
</section>

<section class="sheet business-card">
  <div class="brand">
    <span class="brand-dot"></span>
    <span class="brand-name">Darren Holcomb</span>
    <span class="brand-sub">Realtors</span>
  </div>
  <div class="card-details">
    <p class="person">Darren Holcomb</p>
    <p>Attorney/Broker</p>
    <div class="spacer"></div>
    <p>P: (555) 201-0148</p>
    <p>F: (555) 201-0162</p>
    <p>C: (555) 201-0177</p>
    <p>2817 W. Larkspur Ave Suite B7</p>
    <p>Brenton Ridge, CO 79748</p>
    <p>Darren@PecosPrairieHouses.com</p>
    <p class="web">PecosPrairieHouses.com</p>
  </div>
</section>

<section class="sheet envelope-back">
  <svg class="flap" width="521" height="233" viewBox="0 0 521 233" aria-hidden="true">
    <path d="M0 0 L232 128 Q260.5 142 289 128 L521 0" fill="none" stroke="var(--fold)" stroke-width="2"/>
    <path d="M0 233 L200 112 M521 233 L321 112" fill="none" stroke="#eeeeee" stroke-width="1"/>
  </svg>
  <div class="brand">
    <span class="brand-dot"></span>
  </div>
  <p class="flap-web">www.PecosPrairieHouses.com</p>
</section>

<section class="sheet envelope-front">
  <div class="brand">
    <span class="brand-dot"></span>
    <span class="brand-name">Darren Holcomb</span>
    <span class="brand-sub">Realtors</span>
  </div>
  <p class="footer-line">2817 W. Larkspur Ave Suite B7 Brenton Ridge, CO 79748 &nbsp;|&nbsp; P: (555) 201-0148 &nbsp;|&nbsp; F: (555) 201-0162 &nbsp;|&nbsp; C: (555) 201-0177 &nbsp;|&nbsp; E: Darren@PecosPrairieHouses.com</p>
  <p class="footer-line footer-web">www.PecosPrairieHouses.com</p>
</section>

</body>
</html>
```